kreative Verpackungen für junges Unternehmen
Sehr professionell in der Umsetzung. Bin mit dem Design und der Zusammenarbeit sehr zufrieden, auch wenn es bei der Nachbearbeitung leichte Missverständnisse gab. Definitiv weiter zu empfehlen!
Zielgruppe
Wir sind ein junges Unternehmen und suchen eine ansprechende Gestaltung unserer Verpackung für unser Produkt.
Unsere Zielgruppe sind Mütter mit Kinderwagen, Rad- und Rollerfahrer.
Aufgabenstellung
Es sollte eine positive Stimmung erzeugt werden (z.B. durch eine lachende junge Frau), das Produkt jedoch im Vordergrund stehen. Zusätzlich wäre es gut, wenn eine gewisse Wärmewirkung vermittelt wird. Es handelt sich um einen Handwärmer, welcher an Griffen befestigt werden kann und in einer Box verpackt werden soll mit folgenden Maßen: Breite/Tiefe/Höhe 80mm/60mm/130mm
Wir freuen uns auf eure kreativen Vorschläge!

```html
<!DOCTYPE html>
<html lang="de">
<head>
<meta charset="utf-8">
<title>Griffwärmer – Verpackung</title>
<link rel="stylesheet" href="https://fonts.googleapis.com/css2?family=Oswald:wght@500;600;700&display=swap">
<style>
  :root {
    --stage: #e9ecea;
    --lid-grey-a: #cbc6c3;
    --lid-grey-b: #aaa3a1;
    --orange-deep: #e9531a;
    --orange: #f39a1e;
    --yellow: #fbcd2d;
    --white: #ffffff;
    --ink: #111111;
    --arrow-red: #e8261c;
    --knit-a: #e4ddd5;
    --knit-b: #b5cbd8;
    --product-light: #ecebe7;
    --product-warm: #f07a35;
    --product-cool: #3aa9e4;
  }
  * { margin: 0; padding: 0; box-sizing: border-box; }
  html, body { width: 1200px; height: 848px; overflow: hidden; background: var(--stage); }
  body { font-family: "Oswald", sans-serif; position: relative; }

  .package { position: absolute; left: 100px; top: 34px; width: 1000px; }

  /* Lid */
  .lid {
    position: relative; height: 360px; overflow: hidden;
    background: linear-gradient(135deg, var(--lid-grey-a), var(--lid-grey-b));
    border-top: 10px solid var(--orange-deep);
  }
  .lid__product {
    position: absolute; left: 150px; top: 150px; width: 380px; height: 190px;
    border-radius: 14px;
    background: linear-gradient(90deg, var(--product-warm) 0%, var(--product-light) 35%, var(--product-light) 62%, var(--product-cool) 100%);
  }
  .lid__photo {
    position: absolute; right: 0; top: 0; width: 470px; height: 100%;
    background: linear-gradient(160deg, var(--knit-a) 0%, #d5dfe6 45%, var(--knit-b) 100%);
  }
  .lid__headline {
    position: absolute; left: 46px; top: 70px; color: var(--white);
    transform: rotate(-9deg); transform-origin: left top;
  }
  .lid__title { font-size: 74px; font-weight: 700; line-height: 1; letter-spacing: 0.5px; }
  .lid__tagline { font-size: 28px; font-weight: 600; line-height: 1.15; margin-left: 56px; }
  .lid__icons {
    position: absolute; right: 120px; top: 160px; display: flex; gap: 10px;
    transform: rotate(-9deg);
  }
  .lid__icons .badge { width: 58px; height: 58px; }

  /* Front */
  .front {
    position: relative; height: 420px; overflow: hidden;
  }
  .front__pattern {
    position: absolute; inset: 0;
    background: linear-gradient(120deg, var(--orange-deep) 0%, var(--orange) 40%, var(--yellow) 100%);
  }
  .front__headline { position: absolute; left: 70px; top: 30px; color: var(--white); }
  .front__title { font-size: 96px; font-weight: 600; line-height: 1; }
  .front__subtitle { font-size: 38px; font-weight: 500; line-height: 1.2; margin-top: 4px; }
  .front__icons {
    position: absolute; left: 70px; bottom: 40px; display: flex; gap: 36px;
  }
  .front__icons .badge { width: 180px; height: 180px; }

  .badge {
    border-radius: 50%; background: var(--white);
    display: flex; align-items: center; justify-content: center;
  }
  .badge svg { width: 78%; height: 78%; }
  .sprites { position: absolute; width: 0; height: 0; }
</style>
</head>
<body>

<svg class="sprites" aria-hidden="true">
  <defs>
    <symbol id="turn-arrows" viewBox="0 0 100 100">
      <path d="M30 30 A22 14 0 0 1 70 24" fill="none" stroke="var(--arrow-red)" stroke-width="8"/>
      <path d="M66 14 L78 26 L62 32 Z" fill="var(--arrow-red)"/>
      <path d="M70 40 A22 14 0 0 1 30 46" fill="none" stroke="var(--arrow-red)" stroke-width="8"/>
      <path d="M34 56 L22 44 L38 38 Z" fill="var(--arrow-red)"/>
    </symbol>
    <symbol id="icon-bike" viewBox="0 0 100 100">
      <g fill="none" stroke="var(--ink)" stroke-width="5" stroke-linejoin="round" stroke-linecap="round">
        <circle cx="24" cy="72" r="16"/><circle cx="76" cy="72" r="16"/>
        <path d="M24 72 L40 46 L66 46 L76 72 M40 46 L52 72 L66 46 M36 40 H46 M62 46 L60 36 H70"/>
      </g>
      <use href="#turn-arrows" x="30" y="0" width="46" height="46"/>
    </symbol>
    <symbol id="icon-scooter" viewBox="0 0 100 100">
      <g fill="none" stroke="var(--ink)" stroke-width="5" stroke-linecap="round">
        <circle cx="20" cy="78" r="9"/><circle cx="80" cy="78" r="9"/>
        <path d="M20 78 L30 70 H68 L74 30 M64 30 H84 M74 30 L80 78"/>
      </g>
      <use href="#turn-arrows" x="44" y="4" width="46" height="46"/>
    </symbol>
    <symbol id="icon-pram" viewBox="0 0 100 100">
      <path d="M26 44 H74 A26 22 0 0 1 26 44 Z M52 20 A24 24 0 0 1 76 44 H52 Z" fill="var(--ink)"/>
      <circle cx="34" cy="82" r="8" fill="var(--ink)"/><circle cx="66" cy="82" r="8" fill="var(--ink)"/>
      <use href="#turn-arrows" x="8" y="4" width="46" height="46"/>
    </symbol>
    <symbol id="icon-buggy" viewBox="0 0 100 100">
      <circle cx="44" cy="32" r="7" fill="var(--ink)"/>
      <path d="M30 44 L40 62 H64 L58 44 Z" fill="var(--ink)"/>
      <path d="M28 34 L40 62 M64 62 L84 54" fill="none" stroke="var(--ink)" stroke-width="5" stroke-linecap="round"/>
      <g fill="none" stroke="var(--ink)" stroke-width="4"><circle cx="36" cy="80" r="7"/><circle cx="66" cy="80" r="7"/></g>
      <use href="#turn-arrows" x="6" y="6" width="40" height="40"/>
    </symbol>
  </defs>
</svg>

<main class="package">
  <section class="lid">
    <div class="lid__product" role="img" aria-label="Produktfoto: weißer Griffwärmer am Lenker mit orangefarbenem und blauem Farbschwung"></div>
    <div class="lid__photo" role="img" aria-label="Foto: junge Frau mit Strickmütze und hellblauem Pullover wärmt sich die Hände"></div>
    <div class="lid__headline">
      <h1 class="lid__title">Griffwärmer</h1>
      <p class="lid__tagline">Nie wieder kalte Hände</p>
    </div>
    <div class="lid__icons">
      <span class="badge"><svg><use href="#icon-bike"/></svg></span>
      <span class="badge"><svg><use href="#icon-scooter"/></svg></span>
      <span class="badge"><svg><use href="#icon-pram"/></svg></span>
      <span class="badge"><svg><use href="#icon-buggy"/></svg></span>
    </div>
  </section>

  <section class="front">
    <div class="front__pattern" role="img" aria-label="Hintergrund: Polygonmuster in Orange- und Gelbtönen"></div>
    <div class="front__headline">
      <h2 class="front__title">Einfache Montage</h2>
      <p class="front__subtitle">für Kinderwagen, Fahrrad, Scooter</p>
    </div>
    <div class="front__icons">
      <span class="badge"><svg role="img" aria-label="Fahrrad"><use href="#icon-bike"/></svg></span>
      <span class="badge"><svg role="img" aria-label="Scooter"><use href="#icon-scooter"/></svg></span>
      <span class="badge"><svg role="img" aria-label="Kinderwagen"><use href="#icon-pram"/></svg></span>
      <span class="badge"><svg role="img" aria-label="Buggy"><use href="#icon-buggy"/></svg></span>
    </div>
  </section>
</main>

</body>
</html>
```